"Corporal Finch" is a brand of gummied aids

Corporal Finch is a brand of service men gummies that help our heroes with anxiety, Irritability and hostility brought on by a condition known as PTSD.

I have uploaded example symbols that can be use to discribe the following
Caffeine-Free, No GMO, Sugar Free, Vegan,
Gluten Free, No THC, etc...

Looking for a label for an 8 or 10oz glass jar. The label needs to allow some view at the bottom of the jar to show the gummies.

My vision, and I welcome your, is a
silhouette of various service people saluting a, or various flags.

Each gummy is 15mg 60 count

I've decided to change the band name on the label. The project is a brand of Gummy aids for PTSD sufferers. The New Name: Valor Bites Target: All first responder service people wanting relief with no THC side affects.

Target Market(s)

All service people, Military, Police, Fire fighters, Medics, Nurses, Doctors, First Responders, etc... (Male and Females)

Font styles to use
Serif
Sans Serif

Requirements
Must have
• Correction: The service people don't have to be saluting a flag.
Note. My uploads are examples only.
Should not have
• Cartoons

```html
<!DOCTYPE html>
<html lang="en">
<head>
<meta charset="utf-8">
<title>Corporal Finch – Jar Label and Lid</title>
<link rel="stylesheet" href="https://fonts.googleapis.com/css2?family=Orbitron:wght@700;900&family=Montserrat:wght@500;700;800&family=Open+Sans:wght@600&display=swap">
<style>
  :root {
    --paper: #ffffff;
    --camo-dark: #161716;
    --camo-mid: #2a2c2a;
    --army-green: #2f5a26;
    --leaf-green: #3f7a36;
    --silver: #cfd3d5;
    --snow: #eef0ee;
    --plaque: #3a3c3b;
    --ink: #141514;
    --white: #ffffff;
  }
  html, body {
    margin: 0;
    padding: 0;
    width: 1200px;
    height: 685px;
    overflow: hidden;
    background: var(--paper);
  }
  .artboard { display: block; width: 1200px; height: 685px; }
  .brand-line { font-family: "Orbitron", sans-serif; font-weight: 900; fill: var(--silver); }
  .infused { font-family: "Montserrat", sans-serif; font-weight: 800; fill: var(--white); }
  .claim { font-family: "Open Sans", sans-serif; font-weight: 600; fill: var(--white); font-size: 10.5px; }
  .count-number { font-family: "Orbitron", sans-serif; font-weight: 900; fill: var(--white); }
  .count-unit { font-family: "Montserrat", sans-serif; font-weight: 500; fill: var(--white); font-size: 8px; }
  .dose { font-family: "Montserrat", sans-serif; font-weight: 500; fill: var(--ink); font-size: 12px; }
  .supplement { font-family: "Montserrat", sans-serif; font-weight: 800; fill: var(--ink); font-size: 15px; }
  .lid-count { font-family: "Orbitron", sans-serif; font-weight: 700; fill: var(--white); font-size: 16px; }
  .lid-caption { font-family: "Montserrat", sans-serif; font-weight: 800; fill: var(--army-green); font-size: 28px; }
</style>
</head>
<body>
<svg class="artboard" viewBox="0 0 1200 685" xmlns="http://www.w3.org/2000/svg">
  <defs>
    <linearGradient id="camo-tone" x1="0" y1="0" x2="1" y2="1">
      <stop offset="0" stop-color="#232523"/>
      <stop offset="0.5" stop-color="#1a1b1a"/>
      <stop offset="1" stop-color="#262826"/>
    </linearGradient>
    <clipPath id="lid-clip"><circle cx="874" cy="300" r="218"/></clipPath>
  </defs>

  <!-- Jar label, flat -->
  <g class="jar-label">
    <rect x="74" y="204" width="465" height="354" fill="var(--camo-dark)"/>
    <rect class="camo-field" role="img" aria-label="Dark grey military camouflage pattern"
          x="74" y="204" width="465" height="300" fill="url(#camo-tone)"/>

    <g class="diet-icons">
      <rect x="83" y="207" width="24" height="212" rx="12" fill="#0f100f"/>
      <circle cx="95" cy="226" r="8" fill="none" stroke="#777" stroke-width="1"/><circle cx="95" cy="226" r="3.5" fill="var(--leaf-green)"/>
      <circle cx="95" cy="259" r="8" fill="none" stroke="#777" stroke-width="1"/><circle cx="95" cy="259" r="3.5" fill="var(--leaf-green)"/>
      <circle cx="95" cy="292" r="8" fill="none" stroke="#777" stroke-width="1"/><circle cx="95" cy="292" r="3.5" fill="var(--leaf-green)"/>
      <circle cx="95" cy="325" r="8" fill="none" stroke="#777" stroke-width="1"/><circle cx="95" cy="325" r="3.5" fill="var(--leaf-green)"/>
      <circle cx="95" cy="358" r="8" fill="none" stroke="#777" stroke-width="1"/><circle cx="95" cy="358" r="3.5" fill="var(--leaf-green)"/>
      <circle cx="95" cy="391" r="8" fill="none" stroke="#777" stroke-width="1"/><circle cx="95" cy="391" r="3.5" fill="var(--leaf-green)"/>
    </g>

    <rect class="saluting-silhouettes" role="img" aria-label="White silhouettes of two service members saluting"
          x="104" y="232" width="146" height="262" rx="6" fill="var(--snow)"/>

    <path class="snow-ground" d="M74 430 L110 440 L150 470 L230 480 L300 500 L380 495 L460 505 L539 498 L539 558 L74 558 Z" fill="var(--snow)"/>
    <path class="base-stripe" d="M74 532 L320 532 L340 520 L539 520 L539 546 L330 546 L320 558 L74 558 Z" fill="var(--army-green)"/>
    <rect x="136" y="528" width="186" height="1.5" fill="var(--ink)"/>

    <text class="brand-line" x="272" y="293" textLength="253" lengthAdjust="spacingAndGlyphs" font-size="50">CORPORAL</text>
    <text class="brand-line" x="272" y="375" textLength="253" lengthAdjust="spacingAndGlyphs" font-size="82">FINCH</text>
    <text class="infused" x="393" y="411" text-anchor="middle" textLength="232" lengthAdjust="spacingAndGlyphs" font-size="22">CBD AND CBG INFUSED</text>

    <g class="claim-plaque">
      <rect x="300" y="420" width="200" height="63" rx="5" fill="var(--plaque)" stroke="#555" stroke-width="1"/>
      <text class="claim" x="400" y="440" text-anchor="middle">Specially Formulated to help our heroes</text>
      <text class="claim" x="400" y="455" text-anchor="middle">with anxiety, Irritability and hostility</text>
      <text class="claim" x="400" y="470" text-anchor="middle">brought on by a condition known as PTSD.</text>
    </g>

    <rect class="count-tab" x="96" y="478" width="40" height="68" rx="6" fill="var(--army-green)"/>
    <text class="count-number" x="116" y="520" text-anchor="middle" font-size="26">60</text>
    <text class="count-unit" x="116" y="537" text-anchor="middle">GUMMIES</text>

    <text class="dose" x="143" y="523">15MG PER GUMMY</text>
    <text class="supplement" x="143" y="545" textLength="160" lengthAdjust="spacingAndGlyphs">DIETARY SUPPLEMENT</text>

    <circle class="origin-badge" cx="511" cy="509" r="17" fill="#2a5aa8" stroke="var(--white)" stroke-width="3"/>
  </g>

  <!-- Lid design -->
  <g class="lid-design">
    <rect class="lid-band" x="603" y="242" width="542" height="114" fill="var(--army-green)"/>
    <circle cx="874" cy="300" r="226" fill="var(--army-green)"/>
    <circle class="camo-field" role="img" aria-label="Dark grey military camouflage pattern"
            cx="874" cy="300" r="218" fill="url(#camo-tone)"/>
    <g clip-path="url(#lid-clip)" fill="none" stroke="var(--leaf-green)" stroke-width="3">
      <path d="M705 227 A200 200 0 0 1 823 124"/>
      <path d="M917 120 A200 200 0 0 1 1055 225"/>
    </g>
    <circle class="origin-badge" cx="872" cy="149" r="45" fill="var(--white)"/>
    <circle cx="872" cy="149" r="30" fill="#2a5aa8"/>

    <text class="brand-line" x="708" y="286" textLength="352" lengthAdjust="spacingAndGlyphs" font-size="66">CORPORAL</text>
    <text class="brand-line" x="708" y="377" textLength="352" lengthAdjust="spacingAndGlyphs" font-size="100">FINCH</text>
    <text class="infused" x="884" y="415" text-anchor="middle" textLength="307" lengthAdjust="spacingAndGlyphs" font-size="27">CBD AND CBG INFUSED</text>

    <circle cx="777" cy="468" r="6" fill="var(--white)"/>
    <text class="lid-count" x="880" y="475" text-anchor="middle" textLength="176" lengthAdjust="spacingAndGlyphs">60 GUMMIES | 15MG</text>
    <circle cx="983" cy="468" r="6" fill="var(--white)"/>

    <text class="lid-caption" x="880" y="583" text-anchor="middle">LID DESIGN</text>
  </g>
</svg>
</body>
</html>
```